Tidewell Vitality Autumn Kickoff Quest advertisement design

We need an advertisement for a health, fitness and wellbeing company promoting a new service. The Autumn Kickoff Quest is a 10 week challenge where people choose from 2 program streams - either 1. Fat Loss or 2. Build Lean Muscle. Access to 40 group functional fitness sessions a week, access to exclusive discounts from Brisk Pantry Co. (BPC), discounts on personal training, a targeted gym program, full gym access for the duration of the Challenge and access to Exercise Physiologists and a Sports Dietitian. This is an Tidewell Vitality service co-branded with Brisk Pantry Co.. The final design should be in line with the style guide, be motivating and communicate a point of difference in the fitness industry.

Target Market(s)

men and women ages 30-50yrs, interested in improving their health and lifestyle

Industry/Entity Type

Fitness

Font styles to use
Other font styles liked:
• see style guide

Colors
000000
5c5c5c
9d9d9d
33b8a4
00a990

Requirements
Must have
• professional and exclusive look and feel, motivating tone
Nice to have
• clean design, not too overcrowding, use key pieces of information only and try to stay within the style guide for colour scheme (what is indicated below is the closest pick to our style guide but colour codes are within)
Should not have
• My project should not have any images that cheapen the challenge to look more like a general gym or body sculpting boot camp

```html
<!DOCTYPE html>
<html lang="en">
<head>
<meta charset="utf-8">
<title>Tidewell Vitality – Autumn Kickoff Quest</title>
<link href="https://fonts.googleapis.com/css2?family=Raleway:wght@300;400;500;600&display=swap" rel="stylesheet">
<style>
  :root {
    --black: #000000;
    --ink: #1a1a1a;
    --grey: #5c5c5c;
    --light-grey: #9d9d9d;
    --teal: #33b8a4;
    --teal-deep: #00a990;
    --white: #ffffff;
  }
  * { margin: 0; padding: 0; box-sizing: border-box; }
  html, body { width: 849px; height: 1200px; overflow: hidden; background: var(--black); }
  body { font-family: "Raleway", sans-serif; }

  .poster { position: relative; width: 849px; height: 1200px; background: var(--black); }

  .dotted { position: absolute; left: 22px; right: 22px; border-top: 3px dotted var(--white); }
  .dotted--dark { border-top-color: var(--ink); }

  .headline { position: absolute; top: 68px; left: 0; right: 0; height: 195px; text-align: center; color: var(--white); }
  .headline__lead { margin-top: 32px; font-size: 48px; font-weight: 400; letter-spacing: 2px; }
  .headline__main { margin-top: 4px; font-size: 100px; font-weight: 500; letter-spacing: 6px; color: var(--teal); line-height: 1; }

  .features { position: absolute; top: 297px; left: 22px; right: 22px; height: 693px; background: var(--white); }

  .grid { position: absolute; top: 28px; left: 0; right: 0; height: 540px; }
  .col-rule { position: absolute; top: 40px; width: 3px; height: 440px; background: var(--ink); }
  .row-rule { position: absolute; top: 256px; height: 3px; background: var(--ink); }

  .cell { position: absolute; text-align: center; color: var(--ink); }
  .t-teal { color: var(--teal); }
  .t-big { font-size: 62px; font-weight: 400; line-height: 1; }
  .t-mid { font-size: 44px; font-weight: 400; line-height: 1.05; }
  .t-small { font-size: 26px; font-weight: 500; line-height: 1.2; }
  .t-tiny { font-size: 20px; font-weight: 500; line-height: 1.25; }

  .cell--gym { left: 0; width: 300px; top: 60px; }
  .cell--discounts { left: 0; width: 300px; top: 280px; }
  .cell--sessions { left: 300px; width: 205px; top: 40px; }
  .cell--program { left: 505px; width: 300px; top: 60px; }
  .cell--experts { left: 505px; width: 300px; top: 290px; }

  .sessions__count { font-size: 86px; font-weight: 500; line-height: 1; letter-spacing: 1px; }
  .sessions__count small { font-size: 34px; font-weight: 500; }

  .streams { position: absolute; top: 636px; left: 0; right: 0; height: 54px; background: var(--teal); color: var(--white);
    font-size: 32px; font-weight: 600; letter-spacing: 2px; text-align: center; line-height: 54px; }
  .streams em { font-style: normal; font-size: 22px; font-weight: 500; }

  .brand { position: absolute; top: 1040px; left: 0; right: 0; text-align: center; color: var(--teal);
    font-size: 70px; font-weight: 400; letter-spacing: 4px; }
</style>
</head>
<body>
<main class="poster">
  <div class="dotted" style="top:68px"></div>
  <header class="headline">
    <p class="headline__lead">AUTUMN KICKOFF</p>
    <h1 class="headline__main">QUEST</h1>
  </header>
  <div class="dotted" style="top:262px"></div>

  <section class="features">
    <div class="grid">
      <div class="col-rule" style="left:300px"></div>
      <div class="col-rule" style="left:502px"></div>
      <div class="row-rule" style="left:0;width:300px"></div>
      <div class="row-rule" style="left:505px;width:300px"></div>

      <div class="cell cell--gym">
        <p class="t-mid">FULL</p>
        <p class="t-big t-teal">GYM</p>
        <p class="t-small t-teal">ACCESS</p>
      </div>

      <div class="cell cell--discounts">
        <p class="t-small t-teal">EXCLUSIVE</p>
        <p class="t-tiny">Discounts from</p>
        <p class="t-big t-teal" style="font-size:80px">BPC</p>
        <p class="t-tiny">Brisk Pantry Co.</p>
      </div>

      <div class="cell cell--sessions">
        <p class="sessions__count">40<small>/WK</small></p>
        <p class="t-mid t-teal" style="margin-top:40px">GROUP</p>
        <p class="t-mid t-teal">FITNESS</p>
        <p class="t-small" style="margin-top:24px">Sessions</p>
      </div>

      <div class="cell cell--program">
        <p class="t-small">TARGETED</p>
        <p class="t-big t-teal">GYM</p>
        <p class="t-small">Program</p>
      </div>

      <div class="cell cell--experts">
        <p class="t-big t-teal">ACCESS</p>
        <p class="t-tiny" style="margin-top:6px">Exercise Physiologist</p>
        <p class="t-tiny">&amp; Sports Dietician</p>
      </div>
    </div>

    <div class="dotted dotted--dark" style="top:624px;left:0;right:0"></div>
    <p class="streams">FAT LOSS <em>or</em> BUILD LEAN MUSCLE</p>
    <div class="dotted dotted--dark" style="top:700px;left:0;right:0"></div>
  </section>

  <footer class="brand">Tidewell Vitality</footer>
</main>
</body>
</html>
```